High-end construction company needs a business card design

We need a modern looking business card that draws people in, is memorable and looks so good people will want to sick it on their fridges.
On the first side what is needed are:
Logo
My name - Tomas Verbelk
Title - Managing Director
Website - www.kravel.co.uk
Email - tomas@kravel.co.uk
Telephone - 020 5194 6381
Mobile - 07845319027
On the back side was is needed is a list of all the services we provide:
-Kitchen Renovations
-Bathroom Renovations
-House Renovations
-Garage Conversions
-Extensions
-Loft Conversions
-Conservatories
-Carpentry
-Tiling
-Electrical
-Plumbing & Heating
-Bricklaying
-Landscaping
-Decorating
-Plastering
We would like the colours to be the same shades as on the logo with grey or black for the words.
Target Market(s)
Anyone who needs building work done
Contact Information for Business Card
This business card is for a construction company which strives to deliver excellent service and quality.
The look and feel of the card should represent this.
Requirements
Must have
- On the first side what is needed are:
Logo
My name - Tomas Verbelk
Title - Managing Director
Website - www.kravel.co.uk
Email - tomas@kravel.co.uk
Telephone - 020 5194 6381
Mobile - 07845319027
Nice to have
- Cool looking features

```html
<!DOCTYPE html>
<html lang="en">
<head>
<meta charset="utf-8">
<title>Kravel Construction Ltd – Business Card Options</title>
<link href="https://fonts.googleapis.com/css2?family=Russo+One&family=Chakra+Petch:wght@600&family=Open+Sans:wght@400;700;800&family=Cormorant+SC:wght@600&display=swap" rel="stylesheet">
<style>
  :root {
    --green: #76bd43;
    --dark: #2b2b2b;
    --white: #ffffff;
    --ink: #1e1e1e;
    --rule: #555555;
  }
  html, body {
    margin: 0;
    padding: 0;
    width: 1200px;
    height: 849px;
    overflow: hidden;
    background: var(--white);
  }
  .sheet { display: block; width: 1200px; height: 849px; }
  .sheet-frame { fill: none; stroke: var(--ink); stroke-width: 2; }
  .option-title { font-family: "Russo One", sans-serif; font-size: 62px; fill: var(--ink); text-anchor: middle; }
  .side-label { font-family: "Russo One", sans-serif; font-size: 42px; fill: var(--ink); text-anchor: end; }
  .crop-mark { stroke: var(--ink); stroke-width: 1.5; }
  .card-edge { fill: var(--white); stroke: var(--rule); stroke-width: 1.5; }
  .fill-dark { fill: var(--dark); }
  .fill-green { fill: var(--green); }
  .fill-white { fill: var(--white); }

  .person-name { font-family: "Russo One", sans-serif; font-size: 25px; fill: var(--white); letter-spacing: 0.5px; }
  .person-name--dark { fill: var(--ink); font-size: 31px; }
  .person-role { font-family: "Chakra Petch", sans-serif; font-weight: 600; font-size: 14px; fill: var(--white); }
  .person-role--serif { font-family: "Cormorant SC", serif; font-weight: 600; font-size: 19px; fill: var(--ink); }

  .contact-ring { fill: none; stroke: var(--green); stroke-width: 1.6; }
  .contact-ring--dark { stroke: var(--green); stroke-width: 2; }
  .contact-glyph { fill: var(--green); }
  .contact-text { font-family: "Open Sans", sans-serif; font-weight: 700; font-size: 10.5px; fill: var(--white); }
  .contact-text--dark { font-size: 14px; fill: var(--ink); }

  .brand-name { font-family: "Open Sans", sans-serif; font-weight: 800; fill: var(--green); text-anchor: middle; letter-spacing: 2px; }
  .brand-sub { font-family: "Open Sans", sans-serif; font-weight: 800; fill: var(--green); text-anchor: middle; letter-spacing: 3px; }

  .services-heading { font-family: "Open Sans", sans-serif; font-weight: 700; font-size: 22px; fill: var(--dark); text-anchor: middle; }
  .services-heading--small { font-size: 14px; fill: var(--ink); text-decoration: underline; }
  .service-row { font-family: "Open Sans", sans-serif; font-size: 19.5px; fill: var(--white); text-anchor: middle; }
  .service-row--dark { font-size: 13.5px; fill: var(--ink); }
  .bullet { fill: var(--green); }
  .bullet--dark { fill: var(--ink); }
</style>
</head>
<body>
<svg class="sheet" viewBox="0 0 2296 1624" xmlns="http://www.w3.org/2000/svg">
  <defs>
    <symbol id="icon-phone" viewBox="0 0 24 24">
      <path d="M6.6 10.8a15.1 15.1 0 0 0 6.6 6.6l2.2-2.2a1 1 0 0 1 1-.25 11.4 11.4 0 0 0 3.6.6 1 1 0 0 1 1 1V20a1 1 0 0 1-1 1A17 17 0 0 1 3 4a1 1 0 0 1 1-1h3.5a1 1 0 0 1 1 1c0 1.25.2 2.45.6 3.6a1 1 0 0 1-.25 1z"/>
    </symbol>
    <symbol id="icon-mail" viewBox="0 0 24 24">
      <path d="M3 6h18v12H3z M4.5 7.5v.4L12 13l7.5-5.1v-.4z" fill-rule="evenodd"/>
    </symbol>
    <symbol id="icon-pointer" viewBox="0 0 24 24">
      <path d="M6 3l12 9-5.2.9 3 6.3-2.3 1.1-3-6.3L6 18z"/>
    </symbol>
  </defs>

  <rect class="sheet-frame" x="1" y="1" width="2294" height="1622"/>

  <!-- ===== Option 1 ===== -->
  <text class="option-title" x="1226" y="104">Option -1</text>

  <g class="card card--front-a">
    <rect class="card-edge" x="445" y="134" width="686" height="393"/>
    <rect class="fill-dark" x="445" y="134" width="343" height="393"/>
    <rect class="fill-green" x="780" y="126" width="16" height="68" rx="7"/>
    <rect class="fill-green" x="780" y="466" width="16" height="69" rx="7"/>
    <path class="fill-green" d="M445 193 H472 a16 16 0 0 1 16 16 V437 a16 16 0 0 1 -16 16 H445 Z"/>

    <text class="person-name" x="502" y="217">TOMAS VERBELK</text>
    <text class="person-role" x="503" y="233">Managing Director</text>

    <g class="contact-list">
      <circle class="contact-ring" cx="505" cy="345" r="10"/>
      <use class="contact-glyph" href="#icon-phone" x="499" y="339" width="12" height="12"/>
      <text class="contact-text" x="522" y="349">020 5194 6381 ;  07845319027</text>

      <circle class="contact-ring" cx="505" cy="377" r="10"/>
      <use class="contact-glyph" href="#icon-mail" x="499" y="371" width="12" height="12"/>
      <text class="contact-text" x="522" y="381">tomas@kravel.co.uk</text>

      <circle class="contact-ring" cx="505" cy="408" r="10"/>
      <use class="contact-glyph" href="#icon-pointer" x="499" y="402" width="12" height="12"/>
    </g>

    <g class="brand-lockup">
      <rect class="fill-green" x="949" y="275" width="22" height="22"/>
      <text class="brand-name" x="960" y="356" font-size="46">KRAVEL</text>
      <text class="brand-sub" x="960" y="378" font-size="12.5">CONSTRUCTION LTD</text>
    </g>

    <g class="crop-marks">
      <line class="crop-mark" x1="460" y1="120" x2="460" y2="134"/>
      <line class="crop-mark" x1="1116" y1="120" x2="1116" y2="134"/>
      <line class="crop-mark" x1="460" y1="527" x2="460" y2="541"/>
      <line class="crop-mark" x1="1116" y1="527" x2="1116" y2="541"/>
      <line class="crop-mark" x1="430" y1="150" x2="445" y2="150"/>
      <line class="crop-mark" x1="430" y1="511" x2="445" y2="511"/>
      <line class="crop-mark" x1="1131" y1="150" x2="1146" y2="150"/>
      <line class="crop-mark" x1="1131" y1="511" x2="1146" y2="511"/>
    </g>
  </g>

  <g class="card card--back-a">
    <rect class="fill-dark" x="1339" y="134" width="687" height="393"/>
    <path class="fill-green" d="M1495 134 H1848 L1838 176 Q1835 186 1825 186 H1518 Q1508 186 1505 176 Z"/>
    <text class="services-heading" x="1671" y="173">OUR SERVICES</text>

    <g class="brand-lockup">
      <rect class="fill-green" x="1673" y="214" width="20" height="20"/>
      <text class="brand-name" x="1683" y="295" font-size="40">KRAVEL</text>
      <text class="brand-sub" x="1683" y="307" font-size="10">CONSTRUCTION LTD</text>
    </g>

    <text class="service-row" x="1683" y="365"><tspan class="bullet">● </tspan>Garage Conversions  <tspan class="bullet">● </tspan>Extensions   <tspan class="bullet">● </tspan>Loft Conversions  <tspan class="bullet">● </tspan>Conservatories</text>
    <text class="service-row" x="1673" y="404"><tspan class="bullet">● </tspan>Kitchen Renovations  <tspan class="bullet">● </tspan>Bathroom Renovations   <tspan class="bullet">● </tspan>House Renovations</text>
    <text class="service-row" x="1682" y="443"><tspan class="bullet">● </tspan>Carpentry   <tspan class="bullet">● </tspan>Tiling   <tspan class="bullet">● </tspan>Electrical   <tspan class="bullet">● </tspan>Plumbing &amp; Heating</text>
    <text class="service-row" x="1679" y="483"><tspan class="bullet">● </tspan>Bricklaying   <tspan class="bullet">● </tspan>Landscaping   <tspan class="bullet">● </tspan>Decorating   <tspan class="bullet">● </tspan>Plastering</text>

    <g class="crop-marks">
      <line class="crop-mark" x1="1355" y1="120" x2="1355" y2="134"/>
      <line class="crop-mark" x1="2010" y1="120" x2="2010" y2="134"/>
      <line class="crop-mark" x1="1355" y1="527" x2="1355" y2="541"/>
      <line class="crop-mark" x1="2010" y1="527" x2="2010" y2="541"/>
      <line class="crop-mark" x1="1325" y1="150" x2="1339" y2="150"/>
      <line class="crop-mark" x1="1325" y1="511" x2="1339" y2="511"/>
      <line class="crop-mark" x1="2026" y1="150" x2="2040" y2="150"/>
      <line class="crop-mark" x1="2026" y1="511" x2="2040" y2="511"/>
    </g>
  </g>

  <!-- ===== Option 2 ===== -->
  <text class="option-title" x="1246" y="776">Option -2</text>

  <g class="card card--front-b">
    <rect class="card-edge" x="445" y="828" width="686" height="392"/>
    <path class="fill-green" d="M690 981 H1129 V1136 H818 Z"/>
    <path class="fill-dark" d="M623 980 H690 L818 1136 H750 Z"/>
    <path class="fill-green" d="M445 1042 H592 L628 1088 H445 Z"/>
    <path class="fill-dark" d="M445 1088 H628 L608 1063 H636 L710 1153 H1005 L1058 1221 L445 1220 Z"/>

    <text class="person-name person-name--dark" x="486" y="912">TOMAS VERBELK</text>
    <text class="person-role person-role--serif" x="488" y="930">Managing Director</text>
    <line x1="488" y1="938" x2="623" y2="938" stroke="var(--rule)" stroke-width="1.5"/>
    <line x1="488" y1="938" x2="522" y2="938" stroke="var(--green)" stroke-width="3"/>

    <g class="contact-list">
      <circle class="contact-ring contact-ring--dark" cx="692" cy="1020" r="15"/>
      <use class="contact-glyph" href="#icon-phone" x="683" y="1011" width="18" height="18"/>
      <text class="contact-text contact-text--dark" x="733" y="1018">020 5194 6381 ;  07845319027</text>

      <circle class="contact-ring contact-ring--dark" cx="726" cy="1063" r="15"/>
      <use class="contact-glyph" href="#icon-mail" x="717" y="1054" width="18" height="18"/>
      <text class="contact-text contact-text--dark" x="772" y="1062">tomas@kravel.co.uk</text>

      <circle class="contact-ring contact-ring--dark" cx="760" cy="1107" r="15"/>
      <use class="contact-glyph" href="#icon-pointer" x="751" y="1098" width="18" height="18"/>
      <text class="contact-text contact-text--dark" x="808" y="1107">www.kravel.co.uk</text>
    </g>

    <g class="brand-lockup">
      <rect class="fill-green" x="544" y="1112" width="20" height="20"/>
      <text class="brand-name" x="555" y="1186" font-size="38">KRAVEL</text>
      <text class="brand-sub" x="555" y="1199" font-size="9.5">CONSTRUCTION LTD</text>
    </g>

    <g class="crop-marks">
      <line class="crop-mark" x1="460" y1="814" x2="460" y2="828"/>
      <line class="crop-mark" x1="1116" y1="814" x2="1116" y2="828"/>
      <line class="crop-mark" x1="460" y1="1220" x2="460" y2="1234"/>
      <line class="crop-mark" x1="1116" y1="1220" x2="1116" y2="1234"/>
      <line class="crop-mark" x1="430" y1="844" x2="445" y2="844"/>
      <line class="crop-mark" x1="430" y1="1205" x2="445" y2="1205"/>
      <line class="crop-mark" x1="1131" y1="844" x2="1146" y2="844"/>
      <line class="crop-mark" x1="1131" y1="1205" x2="1146" y2="1205"/>
    </g>
  </g>
  <text class="side-label" x="1105" y="1268">Front</text>

  <g class="card card--back-b">
    <rect class="fill-dark" x="1339" y="828" width="687" height="392"/>
    <path class="fill-white" d="M1421 1021 H1473 L1583 1153 H2026 V1172 H1544 Z"/>
    <path class="fill-green" d="M1503 1011 H2026 V1153 H1615 Z"/>
    <path class="fill-green" d="M1341 1068 H1437 L1470 1108 H1341 Z"/>

    <g class="brand-lockup">
      <rect class="fill-green" x="1680" y="870" width="24" height="24"/>
      <text class="brand-name" x="1692" y="974" font-size="54">KRAVEL</text>
      <text class="brand-sub" x="1692" y="992" font-size="13">CONSTRUCTION LTD</text>
    </g>

    <text class="services-heading services-heading--small" x="1754" y="1027">OUR SERVICES</text>
    <text class="service-row service-row--dark" x="1760" y="1051"><tspan class="bullet--dark">● </tspan>Kitchen Renovations  <tspan class="bullet--dark">● </tspan> Bathroom Renovations   <tspan class="bullet--dark">● </tspan> House Renovations</text>
    <text class="service-row service-row--dark" x="1783" y="1083"><tspan class="bullet--dark">● </tspan>Garage Conversions <tspan class="bullet--dark">● </tspan> Extensions <tspan class="bullet--dark">● </tspan>Loft Conversions <tspan class="bullet--dark">● </tspan>Conservatories</text>
    <text class="service-row service-row--dark" x="1783" y="1116"><tspan class="bullet--dark">● </tspan>Carpentry   <tspan class="bullet--dark">● </tspan>  Tiling   <tspan class="bullet--dark">● </tspan>  Electrical   <tspan class="bullet--dark">● </tspan>  Plumbing &amp; Heating</text>
    <text class="service-row service-row--dark" x="1809" y="1146"><tspan class="bullet--dark">● </tspan>Bricklaying   <tspan class="bullet--dark">● </tspan> Landscaping   <tspan class="bullet--dark">● </tspan> Decorating    <tspan class="bullet--dark">● </tspan> Plastering</text>

    <g class="crop-marks">
      <line class="crop-mark" x1="1355" y1="814" x2="1355" y2="828"/>
      <line class="crop-mark" x1="2010" y1="814" x2="2010" y2="828"/>
      <line class="crop-mark" x1="1355" y1="1220" x2="1355" y2="1234"/>
      <line class="crop-mark" x1="2010" y1="1220" x2="2010" y2="1234"/>
      <line class="crop-mark" x1="1325" y1="844" x2="1339" y2="844"/>
      <line class="crop-mark" x1="1325" y1="1205" x2="1339" y2="1205"/>
      <line class="crop-mark" x1="2026" y1="844" x2="2040" y2="844"/>
      <line class="crop-mark" x1="2026" y1="1205" x2="2040" y2="1205"/>
    </g>
  </g>
  <text class="side-label" x="1990" y="1268">Back</text>
</svg>
</body>
</html>
```